Luxury Jewelry & Watch Company Website Design

At Varrenté, we are a brand that designs and sells unique Jewelry & Watches for Men and Women. We are looking to transform our current e-commerce website, which looks like a boring catalog, into a more EXCLUSIVE, luxurious, and unique website experience... CLASSY, yet MODERN...We want customers/ clients to be drawn into our brand and our products.. essentially to turn them into buying customers. We want them to feel the exclusiveness of our brand and how different we are from the rest of the industry. The website has to convey the feel and culture of our brand, but stay simple to navigate.

We sell direct to the consumer online as well as wholesale to retailers, And now we are opening our first store in March..So the website should appeal to all areas. Id like to have a place on the website for our upcoming store, it would be sweet to have an area where clients can setup an appointment to meet with me at the store to go over and Jewelry, watches, or Custom Jewelry Design. In March, we will have professional photos of the store as well as professional photos of models wearing the Jewelry & Watches. So please make space for all of those new photos to be implemented.

That should be it! It all comes down to creating a Luxurious, Exclusive, and Unique website that portrays Varrenté and brings in clientele and seals the deal for sales!

Thank you very much! We are extremely excited to see all your awesome designs!

Target Market(s)

25-40 year old successful Men & Women... The young professionals crowd.

Industry/Entity Type

E-Commerce

Requirements
Must have
• Luxury, Exclusive feeling (like Corvane, Dorrin Gate Gin, ext), Simplicity, Brand Culture, Watches are our main product, Appeal to both Men & Women. Also, an elegant banner for promotions, that i am able to update myself.
Nice to have
• Store Appointment Scheduler, updated area that shows which celebs/ stars are wearing the goods, History of the brand and products

```html
<!DOCTYPE html>
<html lang="en">
<head>
<meta charset="utf-8">
<title>Varrenté — Watches &amp; Jewellery</title>
<link rel="stylesheet" href="https://fonts.googleapis.com/css2?family=Source+Sans+3:wght@400;600;700&display=swap">
<style>
  :root {
    --ink: #1a1a1a;
    --text: #2b2b2b;
    --muted: #777777;
    --line: #dcdcdc;
    --page: #ffffff;
    --header-top: #ffffff;
    --header-bottom: #e6e6e6;
    --topbar: #3a3a3a;
    --cart-tab: #5e5e5e;
    --button: #444444;
    --footer: #353535;
    --footer-rule: #cfcfcf;
    --footer-text: #e6e6e6;
    --footer-muted: #9a9a9a;
    --footer-logo: #a9a9a9;
  }
  * { box-sizing: border-box; margin: 0; padding: 0; }
  html, body { width: 1200px; height: 2253px; overflow: hidden; }
  body {
    position: relative;
    background: var(--page);
    font-family: "Source Sans 3", sans-serif;
    color: var(--text);
  }

  /* Header */
  .site-header {
    position: absolute; left: 0; top: 0; width: 1200px; height: 125px;
    background: linear-gradient(var(--header-top), var(--header-bottom));
    border-top: 6px solid var(--topbar);
  }
  .brand {
    position: absolute; left: 52px; top: 30px;
    font-size: 48px; line-height: 56px; font-weight: 400; color: var(--ink); letter-spacing: 1px;
  }
  .cart-tab {
    position: absolute; left: 1004px; top: -6px; width: 153px; height: 38px;
    background: var(--cart-tab); border-radius: 0 0 16px 16px;
    color: #f2f2f2; font-size: 13px;
    display: flex; align-items: center; justify-content: center; gap: 10px;
  }
  .main-nav a {
    position: absolute; white-space: nowrap; top: 62px;
    font-size: 19px; line-height: 24px; color: var(--ink); text-decoration: none;
  }
  .main-nav .sep {
    position: absolute; top: 64px; width: 1px; height: 20px; background: #bdbdbd;
  }

  /* Hero */
  .hero {
    position: absolute; left: 0; top: 125px; width: 1200px; height: 644px;
    background:
      linear-gradient(90deg, rgba(20,20,20,0) 0%, rgba(20,20,20,0) 72%, rgba(25,25,25,0.75) 76%, rgba(25,25,25,0.75) 86%, rgba(20,20,20,0) 90%),
      linear-gradient(180deg, #3f3f3f 0%, #6a6a6a 22%, #8d8d8d 34%, #dcdcdc 46%, #c4c4c4 60%, #8a8a8a 72%, #4a4a4a 82%, #7c7c7c 92%, #9a9a9a 100%);
  }
  .hero-dots { position: absolute; left: 570px; top: 620px; display: flex; gap: 6px; }
  .hero-dots span { width: 10px; height: 10px; border-radius: 50%; background: #222; border: 1px solid #fff; }
  .hero-dots span.is-active { background: #f4f4f4; border-color: #aaa; }

  /* Product sections */
  .section-title {
    position: absolute; font-size: 25px; line-height: 30px; font-weight: 600; color: var(--ink);
  }
  .product-card {
    position: absolute; width: 245px; height: 315px;
    background: #fff; border: 1px solid var(--line); border-radius: 3px;
    box-shadow: 0 12px 14px -10px rgba(0,0,0,0.2);
    text-align: center;
  }
  .product-image {
    position: absolute; left: 22px; top: 30px; width: 200px; height: 150px;
  }
  .tone-silver { background: radial-gradient(ellipse 42% 30% at 50% 50%, #a9a9a9 0%, #d6d6d6 55%, rgba(255,255,255,0) 100%); }
  .tone-dark { background: radial-gradient(ellipse 36% 34% at 50% 50%, #1f1f1f 0%, #555 50%, rgba(255,255,255,0) 100%); }
  .tone-steel { background: radial-gradient(ellipse 22% 42% at 50% 50%, #3d4452 0%, #b8bcc4 55%, rgba(255,255,255,0) 100%); }
  .tone-amber { background: radial-gradient(ellipse 44% 28% at 50% 50%, #b5651f 0%, #d9a060 50%, rgba(255,255,255,0) 100%); }
  .tone-gold { background: radial-gradient(ellipse 36% 36% at 50% 52%, #b88a2c 0%, #dcc07a 50%, rgba(255,255,255,0) 100%); }
  .tone-rose { background: radial-gradient(ellipse 42% 24% at 50% 50%, #d89358 0%, #f0c9a2 50%, rgba(255,255,255,0) 100%); }
  .product-name {
    position: absolute; left: 0; right: 0; top: 183px;
    font-size: 19px; line-height: 24px; font-weight: 400; color: var(--ink);
  }
  .product-desc {
    position: absolute; left: 0; right: 0; top: 211px;
    font-size: 12.5px; line-height: 17px; color: var(--muted);
  }
  .product-price {
    position: absolute; left: 30px; top: 255px;
    font-size: 24px; line-height: 30px; color: var(--ink);
  }
  .add-to-cart {
    position: absolute; left: 118px; top: 257px; width: 97px; height: 27px;
    border-radius: 14px; background: var(--button); color: #fff;
    font-size: 12px; line-height: 27px; border: none;
    font-family: "Source Sans 3", sans-serif;
  }

  /* Footer */
  .site-footer {
    position: absolute; left: 0; top: 2070px; width: 1200px; height: 183px;
    background: var(--footer); border-top: 5px solid var(--footer-rule);
  }
  .footer-nav {
    position: absolute; left: 63px; top: 43px;
    font-size: 15px; line-height: 20px; color: var(--footer-text);
  }
  .footer-nav span { margin: 0 7px; }
  .copyright { position: absolute; left: 63px; top: 76px; font-size: 12px; color: var(--footer-muted); }
  .social { position: absolute; left: 65px; top: 106px; display: flex; gap: 6px; }
  .social span { width: 16px; height: 16px; border-radius: 50%; background: #f2f2f2; }
  .footer-brand {
    position: absolute; left: 916px; top: 36px;
    font-size: 42px; line-height: 50px; font-weight: 400; color: var(--footer-logo); letter-spacing: 1px;
  }
</style>
</head>
<body>

<header class="site-header">
  <div class="brand">Varrenté</div>
  <div class="cart-tab">
    <svg width="22" height="18" viewBox="0 0 22 18" aria-hidden="true">
      <path d="M1 2h4l3 10h10l2-7H7" fill="none" stroke="#f2f2f2" stroke-width="1.8"/>
      <circle cx="9" cy="15.5" r="1.6" fill="#f2f2f2"/>
      <circle cx="17" cy="15.5" r="1.6" fill="#f2f2f2"/>
    </svg>
    <span>0 items</span>
  </div>
  <nav class="main-nav">
    <a style="left:470px">Home</a>
    <span class="sep" style="left:536px"></span>
    <a style="left:561px">About Us</a>
    <span class="sep" style="left:655px"></span>
    <a style="left:676px">Our Jewellery</a>
    <span class="sep" style="left:804px"></span>
    <a style="left:826px">Appointment</a>
    <span class="sep" style="left:954px"></span>
    <a style="left:974px">History</a>
    <span class="sep" style="left:1050px"></span>
    <a style="left:1073px">Contact</a>
  </nav>
</header>

<section class="hero" role="img" aria-label="Black and white photograph of a well-dressed man walking beside a classic luxury car in front of a graffiti wall">
  <div class="hero-dots"><span class="is-active"></span><span></span><span></span><span></span></div>
</section>

<h2 class="section-title" style="left:62px;top:806px">Latest Watches</h2>

<article class="product-card" style="left:60px;top:852px">
  <div class="product-image tone-silver" role="img" aria-label="Silver bracelet watch with crystal dial"></div>
  <h3 class="product-name">Product Name</h3>
  <p class="product-desc">Sed metus augue, convallis et,<br>vehicula ut, pulvinar eu, ante.</p>
  <span class="product-price">$25.99</span><button class="add-to-cart">Add to Cart</button>
</article>
<article class="product-card" style="left:337px;top:852px">
  <div class="product-image tone-dark" role="img" aria-label="Black sports chronograph watch"></div>
  <h3 class="product-name">Product Name</h3>
  <p class="product-desc">Sed metus augue, convallis et,<br>vehicula ut, pulvinar eu, ante.</p>
  <span class="product-price">$25.99</span><button class="add-to-cart">Add to Cart</button>
</article>
<article class="product-card" style="left:608px;top:852px">
  <div class="product-image tone-steel" role="img" aria-label="Steel watch with dark blue dial"></div>
  <h3 class="product-name">Product Name</h3>
  <p class="product-desc">Sed metus augue, convallis et,<br>vehicula ut, pulvinar eu, ante.</p>
  <span class="product-price">$25.99</span><button class="add-to-cart">Add to Cart</button>
</article>
<article class="product-card" style="left:883px;top:852px">
  <div class="product-image tone-amber" role="img" aria-label="Bracelet watch set with amber stones"></div>
  <h3 class="product-name">Product Name</h3>
  <p class="product-desc">Sed metus augue, convallis et,<br>vehicula ut, pulvinar eu, ante.</p>
  <span class="product-price">$25.99</span><button class="add-to-cart">Add to Cart</button>
</article>

<h2 class="section-title" style="left:66px;top:1238px">Latest Jewellery</h2>

<article class="product-card" style="left:66px;top:1284px">
  <div class="product-image tone-gold" role="img" aria-label="Gold ring set with diamonds"></div>
  <h3 class="product-name">Product Name</h3>
  <p class="product-desc">Sed metus augue, convallis et,<br>vehicula ut, pulvinar eu, ante.</p>
  <span class="product-price">$25.99</span><button class="add-to-cart">Add to Cart</button>
</article>
<article class="product-card" style="left:343px;top:1284px">
  <div class="product-image tone-silver" role="img" aria-label="Silver jewelled bracelet watch"></div>
  <h3 class="product-name">Product Name</h3>
  <p class="product-desc">Sed metus augue, convallis et,<br>vehicula ut, pulvinar eu, ante.</p>
  <span class="product-price">$25.99</span><button class="add-to-cart">Add to Cart</button>
</article>
<article class="product-card" style="left:614px;top:1284px">
  <div class="product-image tone-gold" role="img" aria-label="Pair of gold wedding bands"></div>
  <h3 class="product-name">Product Name</h3>
  <p class="product-desc">Sed metus augue, convallis et,<br>vehicula ut, pulvinar eu, ante.</p>
  <span class="product-price">$25.99</span><button class="add-to-cart">Add to Cart</button>
</article>
<article class="product-card" style="left:889px;top:1284px">
  <div class="product-image tone-silver" role="img" aria-label="Silver tiara with crystals"></div>
  <h3 class="product-name">Product Name</h3>
  <p class="product-desc">Sed metus augue, convallis et,<br>vehicula ut, pulvinar eu, ante.</p>
  <span class="product-price">$25.99</span><button class="add-to-cart">Add to Cart</button>
</article>

<article class="product-card" style="left:66px;top:1654px">
  <div class="product-image tone-rose" role="img" aria-label="Rose gold flower earrings with diamonds"></div>
  <h3 class="product-name">Product Name</h3>
  <p class="product-desc">Sed metus augue, convallis et,<br>vehicula ut, pulvinar eu, ante.</p>
  <span class="product-price">$25.99</span><button class="add-to-cart">Add to Cart</button>
</article>
<article class="product-card" style="left:343px;top:1654px">
  <div class="product-image tone-silver" role="img" aria-label="White gold diamond engagement ring"></div>
  <h3 class="product-name">Product Name</h3>
  <p class="product-desc">Sed metus augue, convallis et,<br>vehicula ut, pulvinar eu, ante.</p>
  <span class="product-price">$25.99</span><button class="add-to-cart">Add to Cart</button>
</article>
<article class="product-card" style="left:614px;top:1654px">
  <div class="product-image tone-gold" role="img" aria-label="Stack of gold bangles and rings"></div>
  <h3 class="product-name">Product Name</h3>
  <p class="product-desc">Sed metus augue, convallis et,<br>vehicula ut, pulvinar eu, ante.</p>
  <span class="product-price">$25.99</span><button class="add-to-cart">Add to Cart</button>
</article>
<article class="product-card" style="left:889px;top:1654px">
  <div class="product-image tone-silver" role="img" aria-label="Interlocking silver diamond rings"></div>
  <h3 class="product-name">Product Name</h3>
  <p class="product-desc">Sed metus augue, convallis et,<br>vehicula ut, pulvinar eu, ante.</p>
  <span class="product-price">$25.99</span><button class="add-to-cart">Add to Cart</button>
</article>

<footer class="site-footer">
  <nav class="footer-nav">HOME<span>/</span>ABOUT US<span>/</span>OUR JEWELLERY<span>/</span>APPOINTMENT<span>/</span>HISTORY<span>/</span>CONTACT</nav>
  <p class="copyright">© 2012 Company Name.&nbsp; All right reserved Term of Use</p>
  <div class="social" aria-label="Social links"><span></span><span></span><span></span></div>
  <div class="footer-brand">Varrenté</div>
</footer>

</body>
</html>
```